Summer Drinks Flyer for Coffee Shop

We are a coffee shop in London and would like to have a cool and nice flyer for our summer drinks (juices and frozen drink) flyer - see on the attached file for the list

Attached you can find an "attempt" - please note that I would no necessary need the image below.

I also attache our new logo.

thank you

Industry/Entity Type

Coffee Shop

```html
<!DOCTYPE html>
<html lang="en">
<head>
<meta charset="utf-8">
<title>Summer Drinks Menu</title>
<link rel="stylesheet" href="https://fonts.googleapis.com/css2?family=Amatic+SC:wght@400;700&family=Roboto:wght@500;700;900&display=swap">
<style>
  :root {
    --page: #e4e8e8;
    --frame: #95d1e8;
    --panel-top: #0aa3dc;
    --panel-bottom: #177ea6;
    --band: #04a2dd;
    --band-light: #95d1e8;
    --white: #ffffff;
    --frozen: #6b5320;
    --juice: #5cc43a;
    --coffee: #e8342a;
    --mint: #4cc23a;
    --ginger: #f08a2a;
    --yellow: #f2e600;
    --brand: #c19a2e;
  }
  * { margin: 0; padding: 0; box-sizing: border-box; }
  html, body { width: 880px; height: 1200px; overflow: hidden; background: var(--page); }
  .flyer {
    position: absolute; left: 34px; top: 20px;
    width: 812px; height: 1160px;
    background: var(--frame);
    font-family: "Roboto", Arial, sans-serif;
  }
  .panel {
    position: absolute; left: 20px; top: 20px;
    width: 772px; height: 1114px;
    background: linear-gradient(170deg, var(--panel-top) 0%, #0d93c6 45%, var(--panel-bottom) 100%);
    overflow: hidden;
  }
  .band-art { position: absolute; left: 0; top: 0; width: 772px; height: 1114px; }
  .section-title {
    position: absolute; left: 52px;
    font-family: "Amatic SC", "Comic Sans MS", cursive;
    font-weight: 400; font-size: 54px; line-height: 1;
    letter-spacing: 3px; text-transform: lowercase;
    padding-bottom: 2px; border-bottom: 2px solid currentColor;
  }
  .price {
    position: absolute; right: 46px;
    font-weight: 900; font-size: 42px; letter-spacing: 4px; line-height: 1;
  }
  .items {
    position: absolute; left: 52px; list-style: none;
    color: var(--white); font-weight: 700;
    font-size: 29px; letter-spacing: 1.6px; line-height: 39.5px;
  }
  .frozen { color: var(--frozen); }
  .juice { color: var(--juice); }
  .coffee { color: var(--coffee); }
  .note {
    position: absolute; color: var(--white);
    font-weight: 500; font-size: 16px; letter-spacing: 1px;
    transform: translate(-50%, -50%) rotate(-25deg);
    white-space: nowrap;
  }
  .note .mint { color: var(--mint); }
  .note .ginger { color: var(--ginger); }
  .note .syrup { color: var(--coffee); }
  .tagline {
    position: absolute; left: 386px; top: 972px;
    font-family: "Amatic SC", "Comic Sans MS", cursive;
    font-weight: 700; font-size: 62px; letter-spacing: 6px;
    color: var(--yellow); white-space: nowrap; line-height: 1;
    transform: translate(-50%, -50%) rotate(-16deg);
  }
  .brand {
    position: absolute; left: 498px; top: 1008px;
    display: flex; align-items: center; gap: 10px;
    color: var(--brand); font-weight: 500; font-size: 46px; letter-spacing: 1px;
  }
  .brand-dot { width: 26px; height: 26px; border-radius: 50%; background: var(--brand); }
</style>
</head>
<body>
  <main class="flyer">
    <section class="panel">
      <svg class="band-art" viewBox="0 0 772 1114" aria-hidden="true">
        <polygon points="0,1038 772,815 772,1114 0,1114" fill="var(--band)"/>
        <polygon points="90,1114 772,908 772,1114" fill="var(--band-light)"/>
      </svg>

      <h2 class="section-title frozen" style="top:128px">Frozen fruit drinks</h2>
      <p class="price frozen" style="top:134px">£2.95</p>
      <ul class="items" style="top:180px">
        <li>Strawberry and banana,</li>
        <li>pineapple, mango and banana</li>
      </ul>

      <h2 class="section-title juice" style="top:322px">Fruit juices</h2>
      <p class="price juice" style="top:328px">£2.95</p>
      <ul class="items" style="top:374px">
        <li>Orange and carrot</li>
        <li>Orange and pineapple</li>
        <li>Pineapple and apple</li>
        <li>Apple and kiwi</li>
        <li>Carrot and ginger</li>
      </ul>
      <p class="note" style="left:502px;top:487px">Add <span class="mint">mint</span> or <span class="ginger">ginger</span> for free</p>

      <h2 class="section-title coffee" style="top:614px">Iced coffees</h2>
      <p class="price coffee" style="top:620px">£2.45</p>
      <ul class="items" style="top:666px">
        <li>Iced Coffee</li>
        <li>Iced Latte</li>
        <li>Iced Chocolate Drink</li>
      </ul>
      <p class="note" style="left:502px;top:806px">Add <span class="syrup">syrupshot</span> for 10p</p>

      <p class="tagline">new summer drinks menu</p>
      <div class="brand"><span class="brand-dot"></span><span>buonora</span></div>
    </section>
  </main>
</body>
</html>
```